Double-sided half page marketing handout for professional association conference

We need a collatoral piece that will go into conference attendees' registration packets. Handout will be double-sided, half-letter-sized page. Working print area is 8.1" by 5.3" for each side. Can be laid out either vertically or horizontally.

One side of the piece will be focused on my firm's contact information and broad scope of services:

Contact Information:
Halvick Partners LLC
Local Government Consultants
555-314-0297
www.halvickpartners.example
info@halvickpartners.example

Services:
Bond Rating Assessments
Economic Development Consulting
Executive Dashboards
Public Policy Analysis
Governance Training & Support
Strategic Planning & Performance Management

The other side of the piece will focus on the Bond Rating Assessments (see http://www.halvickpartners.example/Pages/Bond-Rating-Assessments.aspx and attachments for more detail). This side should contain the text:

"Considering issuing debt? Bond ratings make a difference. Did you know that on an average $20 million GO debt issuance a one rating-level difference can easily equate to over $350,000 in interest cost-savings under normal market conditions?

The ratings agencies use a combined quantitative and qualitative approach to arrive at your bond rating. Our Bond Ratings Assessment shows you precisely what the agencies are looking at, provides advice as to how to frame the conversation during ratings calls, and identifies both strategic opportunities to provide upgrade pressure and specific threats that may lead to a downgrade. Call or email us to find out more or to get an example assessment."

Go to www.halvickpartners.example and see attached files for logo and a recent winning ArtBazaarly 1/4 page advertisement for style guidance.

Target Market(s)

Highly-educated, conservative local government executives.

Industry/Entity Type

Marketing

Font styles to use
Sans Serif

Colors
3277b5
85acd3
ffffff

Requirements
Must have
• Our logo, our contact information, basic information stated in Project Description. Feel free to modify language to make more clear or understandable.
Nice to have
• We rather not just a text piece - bringing in some graphical elements would be very nice.

```html
<!DOCTYPE html>
<html lang="en">
<head>
<meta charset="utf-8">
<title>Halvick Partners LLC – Conference Handout</title>
<link rel="stylesheet" href="https://fonts.googleapis.com/css2?family=Questrial&display=swap">
<style>
  :root {
    --brand-blue: #3277b5;
    --brand-mid: #4a8cc4;
    --brand-light: #85acd3;
    --white: #ffffff;
    --ink: #333333;
    --logo-grey: #555555;
    --divider-grey: #e3e3e6;
    --page-bg: #eef1f4;
  }
  * { box-sizing: border-box; margin: 0; padding: 0; }
  html, body {
    width: 1200px; height: 1000px; overflow: hidden;
    background: var(--page-bg);
    font-family: "Questrial", "Century Gothic", sans-serif;
  }
  .sheet {
    position: absolute; left: 250px; width: 700px; height: 458px;
    overflow: hidden; box-shadow: 0 4px 14px rgba(0,0,0,.15);
  }
  .sheet--front { top: 28px; background: var(--brand-blue); }
  .sheet--back { top: 514px; background: var(--white); }

  .sheet__art { position: absolute; inset: 0; }

  /* Front side */
  .services-title {
    position: absolute; top: 26px; left: 0; width: 700px; text-align: center;
    color: var(--white); font-size: 34px; letter-spacing: 1px;
  }
  .service-label {
    position: absolute; color: var(--white); font-size: 16px;
    line-height: 1.15; text-transform: uppercase; text-align: center;
  }
  .service-label--left { left: 20px; width: 170px; }
  .service-label--right { right: 20px; width: 180px; }

  .identity {
    position: absolute; left: 210px; top: 118px; width: 280px; text-align: center;
  }
  .identity__name {
    color: var(--logo-grey); font-size: 36px; line-height: 1.05; margin-top: 28px;
  }
  .identity__tagline {
    margin: 14px auto 0; width: 210px; padding-bottom: 6px;
    border-bottom: 1px solid #bbbbbb; color: var(--ink); font-size: 13px;
  }
  .identity__phone {
    margin-top: 10px; color: var(--brand-blue); font-size: 26px; letter-spacing: .5px;
  }
  .identity__web, .identity__email { color: var(--ink); font-size: 12.5px; line-height: 1.3; }

  /* Back side */
  .feature { position: absolute; left: 36px; top: 34px; width: 340px; color: var(--ink); }
  .feature__title { color: var(--brand-blue); font-size: 24px; font-weight: 400; }
  .feature__lead { margin-top: 14px; font-size: 16.5px; line-height: 1.3; }
  .feature__body { margin-top: 18px; font-size: 12px; line-height: 1.35; }

  .service-list {
    position: absolute; left: 432px; top: 54px; width: 248px; list-style: none;
  }
  .service-list__item {
    background: var(--white); color: var(--brand-blue); text-align: center;
    font-size: 13px; line-height: 1.1; padding: 5px 8px; margin-bottom: 8px;
  }
  .visit {
    position: absolute; right: 26px; top: 300px; width: 240px; text-align: right;
    color: var(--white); font-size: 19px; line-height: 1.25; opacity: .92;
  }
</style>
</head>
<body>

<section class="sheet sheet--front" aria-label="Front: services and contact">
  <svg class="sheet__art" width="700" height="458" viewBox="0 0 700 458" aria-hidden="true">
    <defs>
      <linearGradient id="front-shade" x1="0" y1="0" x2="0" y2="1">
        <stop offset="0" stop-color="#3f86c2"/>
        <stop offset="1" stop-color="#2f70aa"/>
      </linearGradient>
    </defs>
    <rect width="700" height="458" fill="url(#front-shade)"/>
    <rect x="0" y="128" width="700" height="52" fill="var(--brand-light)" opacity=".45"/>
    <rect x="0" y="238" width="700" height="52" fill="var(--brand-light)" opacity=".45"/>
    <rect x="0" y="348" width="700" height="52" fill="var(--brand-light)" opacity=".45"/>
    <rect x="470" y="68" width="230" height="50" fill="var(--brand-light)" opacity=".35"/>
    <circle cx="350" cy="262" r="154" fill="var(--brand-light)"/>
    <circle cx="350" cy="262" r="140" fill="var(--white)"/>
  </svg>

  <h1 class="services-title">SERVICES</h1>

  <p class="service-label service-label--left" style="top:138px">Bond Rating<br>Assessments</p>
  <p class="service-label service-label--left" style="top:248px">Public Policy<br>Analysis</p>
  <p class="service-label service-label--left" style="top:358px">Executive<br>Dashboards</p>

  <p class="service-label service-label--right" style="top:66px">Economic<br>Development<br>Consulting</p>
  <p class="service-label service-label--right" style="top:196px">Governance<br>Training &amp;<br>Support</p>
  <p class="service-label service-label--right" style="top:300px">Strategic<br>Planning &amp;<br>Performance<br>Management</p>

  <div class="identity">
    <p class="identity__name">Halvick<br>Partners LLC</p>
    <p class="identity__tagline">Local Government Consultants</p>
    <p class="identity__phone">555-314-0297</p>
    <p class="identity__web">www.halvickpartners.example</p>
    <p class="identity__email">info@halvickpartners.example</p>
  </div>
</section>

<section class="sheet sheet--back" aria-label="Back: Bond Rating Assessments">
  <svg class="sheet__art" width="700" height="458" viewBox="0 0 700 458" aria-hidden="true">
    <rect x="400" y="0" width="20" height="458" fill="var(--divider-grey)"/>
    <rect x="420" y="0" width="280" height="458" fill="var(--brand-mid)"/>
  </svg>

  <article class="feature">
    <h2 class="feature__title">Bond Rating Assessments</h2>
    <p class="feature__lead">Considering issuing debt? Bond ratings make a difference. Did you know that on an average $20 million GO debt issuance a one rating-level difference can easily equate to over $350,000 in interest cost-savings under normal market conditions?</p>
    <p class="feature__body">The ratings agencies use a combined quantitative and qualitative approach to arrive at your bond rating. Our Bond Ratings Assessment shows you precisely what the agencies are looking at, provides advice as to how to frame the conversation during ratings calls, and identifies both strategic opportunities to provide upgrade pressure and specific threats that may lead to a downgrade. Call or email us to find out more or to get an example assessment.</p>
  </article>

  <ul class="service-list">
    <li class="service-list__item">Economic Development<br>Consulting</li>
    <li class="service-list__item">Executive Dashboards</li>
    <li class="service-list__item">Governance Training</li>
    <li class="service-list__item">Strategic Planning &amp;<br>Performance Management</li>
    <li class="service-list__item">Public Policy Analysis</li>
  </ul>

  <p class="visit">Visit us at<br>www.halvickpartners.example<br>to learn more.</p>
</section>

</body>
</html>
```